Business card design needed

I run a Beautician studio (for 7 years now)
I offer
- Vestolin Body Sugaring
- Velumi Glow
- Nails
- Facials
- Manicure
- Foot Treatment
It might not be necessary to list all those treatments?
Maybe the link to the Website is sufficient?
I leave that up to you ...
(more info on www.BuffsAndBrowsByMarisol.com.au)
Vestolin BodySugaring is our biggest success, It replaces waxing.
I would like to incorporate the logo into the Business Card.
We had many complaints regarding our old Business Cards as the Phone Number was to small.
On the backside, we would like a "your next Appointment" section.
Looking forward to you Design, cheers ... Marisol
Buffs by Brows by Marisol
14 Merindo Cct 3912 Berwick
www.BuffsAndBrowsByMarisol.com.au
03 9418 2276

```html
<!DOCTYPE html>
<html lang="en">
<head>
<meta charset="utf-8">
<title>Buffs &amp; Brows by Marisol – Business Card</title>
<link rel="stylesheet" href="https://fonts.googleapis.com/css2?family=Lato:wght@700;900&display=swap">
<style>
  :root {
    --page-bg: #ffffff;
    --card-light: #fbfaf7;
    --card-warm: #e8e4db;
    --strip-bg: #f3f2ef;
    --strip-edge: rgba(0, 0, 0, 0.10);
    --ink: #1f1f1f;
    --bullet: #ee5a2f;
    --petal-orange: #ef6a45;
    --petal-pink: #d9549a;
    --petal-teal: #7fcfdc;
    --stem: #3a3a3a;
  }

  html, body {
    margin: 0;
    padding: 0;
    width: 1200px;
    height: 900px;
    overflow: hidden;
    background: var(--page-bg);
    font-family: "Lato", Arial, sans-serif;
    color: var(--ink);
  }

  .card {
    position: absolute;
    left: 24px;
    top: 94px;
    width: 1152px;
    height: 712px;
    overflow: hidden;
    background:
      radial-gradient(ellipse at 30% 20%, var(--card-light) 0%, var(--card-light) 35%, transparent 75%),
      linear-gradient(160deg, var(--card-light) 0%, #f1efe9 55%, var(--card-warm) 100%);
  }

  .contact-strip {
    position: absolute;
    left: 0;
    top: 0;
    width: 286px;
    height: 100%;
    background: linear-gradient(90deg, #f7f6f3 0%, var(--strip-bg) 100%);
    box-shadow: 6px 0 10px var(--strip-edge);
  }

  .vertical-line {
    position: absolute;
    margin: 0;
    writing-mode: vertical-rl;
    transform: rotate(180deg);
    white-space: nowrap;
    font-weight: 700;
    line-height: 1;
  }

  .website {
    left: 150px;
    bottom: 56px;
    font-size: 29px;
    letter-spacing: 0.2px;
  }

  .phone {
    left: 204px;
    bottom: 76px;
    font-size: 52px;
  }

  .studio-name {
    position: absolute;
    left: 330px;
    top: 92px;
    margin: 0;
    font-size: 54px;
    font-weight: 900;
    letter-spacing: 0.5px;
    line-height: 1;
    white-space: nowrap;
  }

  .treatments {
    position: absolute;
    left: 342px;
    top: 270px;
    margin: 0;
    padding: 0;
    list-style: none;
  }

  .treatments li {
    position: relative;
    padding-left: 22px;
    font-size: 29px;
    font-weight: 700;
    line-height: 42px;
    white-space: nowrap;
  }

  .treatments li::before {
    content: "";
    position: absolute;
    left: 0;
    top: 15px;
    width: 14px;
    height: 14px;
    border-radius: 50%;
    background: var(--bullet);
  }

  .flower-art {
    position: absolute;
    left: 596px;
    top: 156px;
    width: 520px;
    height: 540px;
    border-radius: 40% 45% 30% 35%;
    background:
      radial-gradient(circle at 45% 30%, rgba(239, 106, 69, 0.55) 0%, transparent 35%),
      radial-gradient(circle at 85% 55%, rgba(217, 84, 154, 0.40) 0%, transparent 30%),
      radial-gradient(circle at 25% 70%, rgba(127, 207, 220, 0.45) 0%, transparent 30%),
      radial-gradient(ellipse at 50% 60%, rgba(120, 120, 120, 0.12) 0%, transparent 70%);
  }
</style>
</head>
<body>
  <article class="card">
    <aside class="contact-strip">
      <p class="vertical-line website">www.BuffsAndBrowsByMarisol.com.au</p>
      <p class="vertical-line phone">Phone: 03 9418 2276</p>
    </aside>

    <h1 class="studio-name">BUFFS &amp; BROWS BY MARISOL</h1>

    <ul class="treatments">
      <li>Vestolin Body Sugaring</li>
      <li>Velumi Glow</li>
      <li>Nails</li>
      <li>Facials</li>
      <li>Manicure</li>
      <li>Foot Treatment</li>
    </ul>

    <div class="flower-art" role="img" aria-label="Illustration of stylised flowers with orange, pink and teal petals on curling dark stems, over faint grey daisies"></div>
  </article>
</body>
</html>
```